LinkedIn Launch Campaign - Info Graphics / Email Template

velvetrip Bookings is a full end to end travel management solution for companies spending between 50k - 8 million a year on travel.

Our software helps companies manage their travel spend and helps employees book their business travel easily.

We are planning to launch our product via LinkedIn in Jan. The launch campaign will run for 2 weeks which we will be posting 6 info-graphics that outline some of the key functionality of our product. These info-graphics need to carry a similar feeling/look and theme as our website (velvetripbookings.com.au).

After the campaign is completed we will then shoot off a HTML email to people to provide more details about us and if they need more info they can get in contact with us.

The info-graphics need to be witty, fun, smart and catchy... They really need to grab peoples attention. The graphics need to marry in with the copy and statement.

Please see below the copy for each graphics, we have text for each graphic but we are unsure if we place the text in the graphic or have this typed into the post on linkedin.

So we will need 6 Info-Graphics designed and 2 email template designs.

Headline Statement – This will be posted regularly so it needs to awesome and very eye catching.

*velvetrip Bookings. Ridiculously easy low cost business travel
Budget- Book – Manage

================================================

*Stop Killing Time - Streamline Travel

velvetrip Bookings. Ridiculously easy low cost business travel
Budget- Book – Manage
TEXT:
Tired of manually managing every little trip detail from multiple platforms? Consolidate all your travel details in one place.

*Save That Cash for Your Bottom Line

Budget- Book – Manage

TEXT:
No more shopping around for deals. Get the most reasonable offers with super low fees on everything from flights, hotel accommodations to vehicle rentals in one click.

* Know What You Spend at a Glance

Budget- Book – Manage
TEXT:
Budget in real-time without the fear of overspending. Track spending, view reports, upload forecasts, and much more from our easy-to-read dashboard.

*Achieve Seamless Travel Compliance

Budget- Book – Manage

TEXT:
In real time track compliance to your travel policy for a stress-free relationship with employees. Be transparent with your employees, set spending limits, and always be audit ready.

=================================================

*Skip the Learning Curve
Budget- Book – Manage

TEXT:
No more boring training sessions! Employees can start using our intuitive interface right away. Spend less time learning a new platform and more time using it.

Project Deadline Extended Reason: We want to extend the deadline to give people more time to work on our project. Also due to the time of year we understand people may be away and will need more time. Added Wednesday, December 28, 2016

Target Market(s)

Target Audience
Mainly Accountants, VP Finance, Bookkeepers, Finance Manager, Senior Management

Industry/Entity Type

Business

Font styles to use
Serif
Sans Serif

Requirements
Must have
• We must use the same feeling / theme / look / as our website.
• It needs to be witty/ modern / smart / fun
• Needs to be simple and clean, like our website.
• Graphics need to connect with the statement / words.
• Needs to be eye catching/ stand out. We like our current colour pallet on our website but we can vary from it so the images are individual and not all the same

```html
<!DOCTYPE html>
<html lang="en">
<head>
<meta charset="utf-8">
<title>velvetrip Bookings – Stop Killing Time banners</title>
<link rel="stylesheet" href="https://fonts.googleapis.com/css2?family=Montserrat:wght@400;600;700;800&family=Open+Sans:wght@400;600&display=swap">
<style>
  :root {
    --canvas: #ffc27d;
    --navy: #1d2a4d;
    --sky-top: #1a2344;
    --sky-mid: #3a4677;
    --horizon: #f39a3c;
    --glow: #ffd27a;
    --ground: #1c2033;
    --accent: #36a9e1;
    --white: #ffffff;
    --muted: #6a7390;
  }
  * { box-sizing: border-box; margin: 0; padding: 0; }
  html, body { width: 900px; height: 1200px; overflow: hidden; }
  body {
    background: var(--canvas);
    font-family: "Open Sans", Arial, sans-serif;
    position: relative;
  }
  .banner {
    position: absolute;
    left: 90px;
    width: 720px;
    overflow: hidden;
  }
  .banner--top { top: 228px; height: 262px; }
  .banner--bottom { top: 498px; height: 232px; }
  .banner__photo {
    position: absolute; inset: 0;
    background:
      radial-gradient(ellipse 60% 30% at 45% 58%, var(--glow) 0%, rgba(243,154,60,0.7) 30%, rgba(243,154,60,0) 70%),
      linear-gradient(180deg, var(--sky-top) 0%, var(--sky-mid) 38%, var(--horizon) 56%, #5a3d4a 64%, var(--ground) 80%, #12141f 100%);
  }
  .tag-band {
    position: absolute;
    right: 0;
    width: 510px;
    height: 52px;
    background: var(--white);
    display: flex;
    align-items: center;
    justify-content: flex-end;
    padding-right: 18px;
    gap: 16px;
  }
  .banner--top .tag-band { top: 0; clip-path: polygon(0 0, 100% 0, 100% 100%, 4% 100%); }
  .banner--bottom .tag-band { bottom: 10px; clip-path: polygon(4% 0, 100% 0, 100% 100%, 0 100%); }
  .tagline { text-align: right; font-family: "Montserrat", Arial, sans-serif; }
  .tagline__main { font-size: 17px; font-weight: 800; color: var(--navy); letter-spacing: -0.2px; }
  .tagline__main .easy { color: var(--accent); font-weight: 600; }
  .tagline__steps { font-size: 9px; font-weight: 600; color: var(--muted); margin-top: 1px; }
  .brand {
    display: flex; align-items: center; gap: 6px;
    font-family: "Montserrat", Arial, sans-serif;
    font-size: 11px; font-weight: 700; color: var(--navy);
  }
  .brand__dot { width: 24px; height: 24px; border-radius: 50%; background: var(--accent); }
  .copy {
    position: absolute;
    left: 30px;
    width: 330px;
    color: var(--white);
  }
  .banner--top .copy { top: 96px; }
  .banner--bottom .copy { top: 26px; }
  .copy__headline {
    font-family: "Montserrat", Arial, sans-serif;
    font-weight: 700;
    font-size: 20px;
    line-height: 1.2;
    margin-bottom: 10px;
  }
  .copy__text { font-size: 10.5px; line-height: 1.45; margin-bottom: 16px; }
  .btn {
    display: inline-block;
    border: 1.5px solid var(--white);
    padding: 8px 12px;
    font-family: "Montserrat", Arial, sans-serif;
    font-size: 9px;
    font-weight: 700;
    letter-spacing: 0.5px;
    color: var(--white);
    text-decoration: none;
  }
</style>
</head>
<body>

<section class="banner banner--top">
  <div class="banner__photo" role="img" aria-label="Sunset view of the horizon above the clouds from an aircraft window, with the wing tip at the right"></div>
  <div class="tag-band">
    <div class="tagline">
      <p class="tagline__main">Ridiculously <span class="easy">easy</span> low cost business travel</p>
      <p class="tagline__steps">Budget · Book · Manage</p>
    </div>
    <div class="brand"><span class="brand__dot"></span>velvetrip Bookings</div>
  </div>
  <div class="copy">
    <h1 class="copy__headline">Stop Killing Time - Streamline Travel</h1>
    <p class="copy__text">Tired of manually managing every little trip detail from multiple platforms? Consolidate all your travel details in one place.</p>
    <a class="btn" href="#">VIEW INFO</a>
  </div>
</section>

<section class="banner banner--bottom">
  <div class="banner__photo" role="img" aria-label="Sunset view of the horizon above the clouds from an aircraft window, with the wing tip at the right"></div>
  <div class="copy">
    <h2 class="copy__headline">Stop Killing Time - Streamline Travel</h2>
    <p class="copy__text">Tired of manually managing every little trip detail from multiple platforms? Consolidate all your travel details in one place.</p>
    <a class="btn" href="#">VIEW INFO</a>
  </div>
  <div class="tag-band">
    <div class="tagline">
      <p class="tagline__main">Ridiculously <span class="easy">easy</span> low cost business travel</p>
      <p class="tagline__steps">Budget · Book · Manage</p>
    </div>
    <div class="brand"><span class="brand__dot"></span>velvetrip Bookings</div>
  </div>
</section>

</body>
</html>
```